Roadmap for an eCourse to be used in the wine industry

I created an online course called Using LedgerLark in the Wine Industry Workshop. This Roadmap shows the flow of the modules and where the coaching calls fit in. Use the attached design from the Lesson Maker's Pathway as a guide, but add icons for the wine industry. List the modules and coaching/consulting calls as shown on the Roadmap List document. I have also attached my logo and business card layout. Please use the same font and colors.

Target Market(s)

Owners and office managers of wineries. These wineries are essentially mom-and-pop size businesses, not large corporations.

Industry/Entity Type

Industry

Font styles to use
Other font styles liked:
• see business card

Requirements
Must have
• Professional look, but not stiff. Wine theme, but not cutesy.
• Font should match or complement the business card
• Color should match the business card and website. www.FTvineyardPartners.com
Nice to have
• The look and feel of the sample Lesson Maker's Pathway works well.

```html
<!DOCTYPE html>
<html lang="en">
<head>
<meta charset="utf-8">
<title>Wine Industry Workshop Roadmap</title>
<link rel="stylesheet" href="https://fonts.googleapis.com/css2?family=Open+Sans:ital,wght@0,400;0,700;1,400&display=swap">
<style>
  :root {
    --bg-top: #ffffff;
    --bg-bottom: #cde6d6;
    --road: #d9d9d9;
    --road-dash: #7a7a7a;
    --banner: #2d6b43;
    --welcome: #6f3a45;
    --plum: #7e4a64;
    --berry: #a05680;
    --rose: #cf86a8;
    --blush: #dbb2c6;
    --magenta: #a8357c;
    --green-light: #b9d63a;
    --green-dark: #7cad30;
    --ink-dark: #3b2a31;
    --ink-light: #ffffff;
    --icon-gold: #e2c07e;
    --icon-wine: #7a3b48;
    --icon-green: #2b5a3c;
    --logo: #6b6b6b;
  }
  html, body { margin: 0; padding: 0; overflow: hidden; }
  body { width: 1200px; height: 927px; }
  .roadmap {
    display: block;
    width: 1200px;
    height: 927px;
    font-family: "Open Sans", Arial, sans-serif;
  }
  .stop-title { font-weight: 700; font-size: 24px; }
  .stop-text { font-weight: 400; font-size: 23px; }
  .stop-big { font-weight: 700; font-size: 28px; }
  .on-dark { fill: var(--ink-light); }
  .on-light { fill: var(--ink-dark); }
  .banner-text { fill: #fff; font-size: 28px; }
  .banner-text .strong { font-weight: 700; }
  .site { font-size: 15px; font-style: italic; fill: #555; }
  .site .strong { font-weight: 700; fill: var(--banner); }
  .logo-name { font-size: 15px; font-weight: 700; fill: var(--logo); letter-spacing: 1px; }
</style>
</head>
<body>
<svg class="roadmap" viewBox="0 0 1500 1159" xmlns="http://www.w3.org/2000/svg">
  <defs>
    <linearGradient id="bg" x1="0" y1="0" x2="0" y2="1">
      <stop offset="0" stop-color="var(--bg-top)"/>
      <stop offset="1" stop-color="var(--bg-bottom)"/>
    </linearGradient>
    <radialGradient id="coach" cx="0.4" cy="0.3" r="0.8">
      <stop offset="0" stop-color="var(--green-light)"/>
      <stop offset="1" stop-color="var(--green-dark)"/>
    </radialGradient>
  </defs>

  <rect class="backdrop" width="1500" height="1159" fill="url(#bg)"/>

  <!-- road -->
  <g class="road" fill="none" stroke-linecap="round" stroke-linejoin="round">
    <path id="road-path" stroke="var(--road)" stroke-width="82"
      d="M235,290 C400,320 450,340 580,335 C700,330 760,300 870,300 C980,300 1050,280 1290,300 C1400,310 1400,420 1330,480 C1280,520 1200,515 1125,510 C1000,500 900,530 765,540 C600,550 500,500 380,500 C250,500 160,520 150,600 C140,700 230,750 315,750 L570,750 C650,750 700,735 777,740 C880,750 930,775 1005,760 C1100,740 1180,700 1275,710 C1360,720 1340,830 1300,880 C1270,930 1250,960 1200,975 C1100,985 1000,985 920,985 C800,985 700,990 575,990 C450,990 300,975 183,975"/>
    <path stroke="var(--road-dash)" stroke-width="7" stroke-dasharray="10 18"
      d="M235,290 C400,320 450,340 580,335 C700,330 760,300 870,300 C980,300 1050,280 1290,300 C1400,310 1400,420 1330,480 C1280,520 1200,515 1125,510 C1000,500 900,530 765,540 C600,550 500,500 380,500 C250,500 160,520 150,600 C140,700 230,750 315,750 L570,750 C650,750 700,735 777,740 C880,750 930,775 1005,760 C1100,740 1180,700 1275,710 C1360,720 1340,830 1300,880 C1270,930 1250,960 1200,975 C1100,985 1000,985 920,985 C800,985 700,990 575,990 C450,990 300,975 183,975"/>
  </g>

  <!-- header -->
  <g class="brand">
    <circle cx="755" cy="86" r="60" fill="none" stroke="var(--logo)" stroke-width="3"/>
    <text class="logo-name" x="755" y="82" text-anchor="middle">VINEYARD</text>
    <text class="logo-name" x="755" y="102" text-anchor="middle">PARTNERS</text>
  </g>
  <g class="title-banner">
    <path d="M960,44 H1500 V106 H960 A31,31 0 0 1 960,44 Z" fill="var(--banner)"/>
    <text class="banner-text" x="983" y="84"><tspan class="strong">Wine Industry</tspan> Workshop Roadmap</text>
  </g>

  <!-- icons (flat placeholders) -->
  <g class="icons">
    <rect role="img" aria-label="Wine bottle beside stacked barrels on a brick wall" x="200" y="135" width="140" height="105" rx="18" fill="var(--icon-gold)"/>
    <rect role="img" aria-label="Document with grape leaf" x="530" y="192" width="90" height="85" rx="10" fill="var(--icon-gold)"/>
    <rect role="img" aria-label="Corkscrew" x="840" y="185" width="65" height="60" rx="12" fill="var(--icon-gold)"/>
    <rect role="img" aria-label="Colour swatches" x="1282" y="198" width="95" height="85" rx="12" fill="var(--icon-gold)"/>
    <rect role="img" aria-label="Report with bar chart and grape leaf" x="1075" y="398" width="80" height="80" rx="10" fill="var(--icon-gold)"/>
    <circle role="img" aria-label="Bunch of grapes" cx="752" cy="440" r="36" fill="var(--icon-gold)"/>
    <rect role="img" aria-label="Point of sale register" x="345" y="410" width="72" height="65" rx="10" fill="var(--icon-gold)"/>
    <rect role="img" aria-label="Sparkling wine bottle" x="296" y="630" width="40" height="92" rx="14" fill="var(--icon-green)"/>
    <rect role="img" aria-label="Barrel with rising chart arrow" x="505" y="643" width="110" height="80" rx="14" fill="var(--icon-wine)"/>
    <rect role="img" aria-label="Standing corkscrew" x="972" y="630" width="68" height="80" rx="12" fill="var(--icon-wine)"/>
    <circle role="img" aria-label="Light bulb with magnifier" cx="1278" cy="662" r="40" fill="var(--icon-gold)"/>
    <rect role="img" aria-label="Tax document under a magnifier" x="875" y="860" width="105" height="80" rx="12" fill="var(--icon-gold)"/>
    <rect role="img" aria-label="Stacked wine bottles" x="520" y="892" width="108" height="75" rx="12" fill="var(--icon-green)"/>
    <rect role="img" aria-label="Two wine glasses toasting" x="115" y="852" width="140" height="95" rx="18" fill="var(--icon-wine)"/>
  </g>

  <!-- stops -->
  <g class="stops" text-anchor="middle">
    <circle cx="237" cy="285" r="81" fill="var(--welcome)"/>
    <text class="stop-big on-dark" x="237" y="268">Welcome</text>
    <text class="stop-big on-dark" x="237" y="293">&amp;</text>
    <text class="stop-big on-dark" x="237" y="318">Foundation</text>

    <circle cx="580" cy="335" r="82" fill="var(--plum)"/>
    <text class="stop-title on-dark" x="580" y="322">Module 1</text>
    <text class="stop-text on-dark" x="580" y="347">Create the</text>
    <text class="stop-text on-dark" x="580" y="371">mini file</text>

    <circle cx="871" cy="302" r="81" fill="var(--plum)"/>
    <text class="stop-title on-dark" x="871" y="281">Module 2</text>
    <text class="stop-text on-dark" x="871" y="306">Enter some</text>
    <text class="stop-text on-dark" x="871" y="330">transactions</text>

    <circle cx="1086" cy="281" r="65" fill="url(#coach)"/>
    <text class="stop-title on-dark" x="1086" y="262">1-on-1</text>
    <text class="stop-title on-dark" x="1086" y="291">Coaching</text>
    <text class="stop-title on-dark" x="1086" y="320">Call</text>

    <circle cx="1293" cy="318" r="82" fill="var(--plum)"/>
    <text class="stop-title on-dark" x="1293" y="311">Module 3</text>
    <text class="stop-text on-dark" x="1293" y="336">Customize</text>
    <text class="stop-text on-dark" x="1293" y="360">the sample</text>
    <text class="stop-text on-dark" x="1293" y="384">file</text>

    <circle cx="1124" cy="508" r="82" fill="var(--berry)"/>
    <text class="stop-title on-dark" x="1124" y="511">Module 4</text>
    <text class="stop-text on-dark" x="1124" y="536">Create</text>
    <text class="stop-text on-dark" x="1124" y="560">Reports</text>

    <circle cx="765" cy="537" r="96" fill="var(--berry)"/>
    <text class="stop-title on-dark" x="765" y="513">Module 5</text>
    <text class="stop-text on-dark" x="765" y="538">Bank and</text>
    <text class="stop-text on-dark" x="765" y="562">credit card</text>
    <text class="stop-text on-dark" x="765" y="586">reconciliations</text>

    <circle cx="381" cy="508" r="82" fill="var(--berry)"/>
    <text class="stop-title on-dark" x="381" y="502">Module 6</text>
    <text class="stop-text on-dark" x="381" y="527">POS</text>
    <text class="stop-text on-dark" x="381" y="551">integration</text>

    <circle cx="134" cy="561" r="82" fill="url(#coach)"/>
    <text class="stop-big on-dark" x="134" y="539">1-on-1</text>
    <text class="stop-big on-dark" x="134" y="569">Coaching</text>
    <text class="stop-big on-dark" x="134" y="599">Call</text>

    <circle cx="314" cy="753" r="82" fill="var(--rose)"/>
    <text class="stop-title on-light" x="314" y="750">Module 7</text>
    <text class="stop-text on-light" x="314" y="775">Customer</text>
    <text class="stop-text on-light" x="314" y="799">Job Flags</text>

    <circle cx="569" cy="751" r="82" fill="var(--rose)"/>
    <text class="stop-title on-light" x="569" y="756">Module 8</text>
    <text class="stop-text on-light" x="569" y="781">Budget &amp;</text>
    <text class="stop-text on-light" x="569" y="805">Forecast</text>

    <circle cx="777" cy="735" r="65" fill="url(#coach)"/>
    <text class="stop-title on-dark" x="777" y="716">1-on-1</text>
    <text class="stop-title on-dark" x="777" y="745">Coaching</text>
    <text class="stop-title on-dark" x="777" y="774">Call</text>

    <circle cx="1006" cy="745" r="65" fill="var(--rose)"/>
    <text class="stop-title on-light" x="1006" y="737">Module 9</text>
    <text class="stop-text on-light" x="1006" y="763">Tips &amp;</text>
    <text class="stop-text on-light" x="1006" y="787">Tricks</text>

    <circle cx="1275" cy="737" r="82" fill="var(--rose)"/>
    <text class="stop-title on-light" x="1275" y="733">Module 10</text>
    <text class="stop-text on-light" x="1275" y="758">More Tips &amp;</text>
    <text class="stop-text on-light" x="1275" y="782">Tricks</text>

    <circle cx="1237" cy="972" r="82" fill="url(#coach)"/>
    <text class="stop-big on-dark" x="1237" y="950">1-on-1</text>
    <text class="stop-big on-dark" x="1237" y="980">Coaching</text>
    <text class="stop-big on-dark" x="1237" y="1010">Call</text>

    <circle cx="921" cy="982" r="82" fill="var(--blush)"/>
    <text class="stop-title on-light" x="921" y="967">Module 11</text>
    <text class="stop-text on-light" x="921" y="992">Book Cost</text>
    <text class="stop-text on-light" x="921" y="1016">vs</text>
    <text class="stop-text on-light" x="921" y="1040">Tax Cost</text>

    <circle cx="574" cy="992" r="82" fill="var(--blush)"/>
    <text class="stop-title on-light" x="574" y="1003">Module 12</text>
    <text class="stop-text on-light" x="574" y="1028">Next Steps</text>

    <circle cx="183" cy="974" r="78" fill="var(--magenta)"/>
    <text class="stop-big on-dark" x="183" y="968">Uncork</text>
    <text class="stop-big on-dark" x="183" y="993">Greater</text>
    <text class="stop-big on-dark" x="183" y="1018">Profits</text>
  </g>

  <text class="site" x="68" y="1111">www.<tspan class="strong">FTvineyard</tspan>Partners.com</text>
</svg>
</body>
</html>
```